Business Card For Video Production Company

Please NOTE: I've added some info to the must haves that I should have included at the start. Thank you.

I need a business card design for my video production company based in Orlando called Caldera Film Works. Our work consists of web video marketing (web videos), training videos, sales videos, conference and seminar video production...basically a lot of corporate based work.

We work with successful small businesses, not-for-profits and some Fortune 500 type groups. We bring a lot of knowledge, experience and attention to detail to every project.

I'd like something that communicates strength, confidence, integrity, as well as creative vision. I want to stay away from the standard icons of the media and film industry. I'd like to emphasize the colors of my logo, and also the colors of my website which has a white background. Simple is good.

Our budgets are moderate...generally $1500 to $5000.

www.calderafilm.tv

PS...We don't do weddings or recitals, or that type of production.
Updates

I want to thank all the designers for your updates. There's way too many to be able to give feedback on for all. I hope you understand that. But wow…there are so many great designs everyone has offered. I can't thank you enough…each and everyone. I hope to make my decision soon. I'm not accepting anymore designs from new designers. Brent-

Target Market(s)

Successful small businesses, marketing directors, corporate communication directors, training and human resources professionals. forward thinking not-for profits. Since my company is based in Central Florida, most of my work comes from this area too.

Industry/Entity Type

Marketing

Requirements
Must have
• website address, www.calderafilm.tv
phone number, 407-552-9031
email address, brent@calderafilm.tv

Title
Brent Caldera
Owner/Creative Director

I'd like to have a single line that goes across illustrating our services, maybe separated with bullet points:

Marketing Videos, Corporate Videos, Conference & Seminar Video Production
Should not have
• No film or video icons.
No need to pull language or copy from my website.

```html
<!DOCTYPE html>
<html lang="en">
<head>
<meta charset="utf-8">
<title>Caldera Film Works – Business Card</title>
<link rel="stylesheet" href="https://fonts.googleapis.com/css2?family=Open+Sans:wght@400;600;700&display=swap">
<style>
  :root {
    --backdrop: #ecebe8;
    --card-white: #ffffff;
    --card-grey: #949598;
    --brand-blue: #1a8fd8;
    --brand-blue-light: #7fc6ee;
    --ink-dark: #3b3d40;
    --ink-mid: #6b6d70;
    --rule: #c9cacc;
  }
  * { box-sizing: border-box; margin: 0; padding: 0; }
  html, body {
    width: 1200px; height: 829px; overflow: hidden;
    background: var(--backdrop);
    font-family: "Open Sans", Arial, sans-serif;
  }
  .stage {
    position: relative; width: 1200px; height: 829px;
    display: flex; align-items: center; justify-content: center; gap: 50px;
  }
  .card {
    position: relative; width: 520px; height: 297px;
    border-radius: 4px; overflow: hidden;
    box-shadow: 0 6px 18px rgba(0,0,0,0.12);
  }
  /* Front */
  .card--front { background: var(--card-white); }
  .edge-tab {
    position: absolute; background: var(--brand-blue); border-radius: 6px;
  }
  .edge-tab--top { right: -6px; top: 14px; width: 16px; height: 92px; }
  .edge-tab--bottom { left: -6px; bottom: 34px; width: 16px; height: 92px; }
  .brand {
    position: absolute; left: 0; right: 0; top: 42px;
    display: flex; align-items: center; justify-content: center; gap: 10px;
  }
  .brand__mark { width: 18px; height: 18px; background: var(--brand-blue); }
  .brand__name {
    font-weight: 700; font-size: 25px; color: var(--ink-dark); letter-spacing: -0.3px;
  }
  .details {
    position: absolute; left: 0; right: 0; top: 108px;
    display: flex; justify-content: center; align-items: stretch;
  }
  .person { text-align: right; padding-right: 16px; padding-top: 20px; }
  .person__name { font-weight: 700; font-size: 17px; color: var(--brand-blue); }
  .person__title { font-size: 12.5px; color: var(--ink-mid); margin-top: 2px; }
  .divider { width: 1px; background: var(--rule); }
  .contact { list-style: none; padding-left: 12px; padding-top: 6px; }
  .contact__item {
    display: flex; align-items: center; gap: 6px;
    font-size: 12px; color: var(--ink-dark); line-height: 22px;
  }
  .contact__icon { width: 13px; height: 13px; flex: none; }
  .services {
    position: absolute; left: 24px; right: 24px; bottom: 44px;
    text-align: center; font-size: 12px; color: var(--brand-blue);
    white-space: nowrap;
  }
  .services__item + .services__item::before {
    content: "•"; margin: 0 5px 0 6px; color: var(--brand-blue-light);
  }
  /* Back */
  .card--back {
    background: var(--card-grey);
    display: flex; flex-direction: column; align-items: center; justify-content: center;
  }
  .back-brand { display: flex; align-items: center; gap: 14px; margin-top: -10px; }
  .back-brand__mark { width: 30px; height: 30px; background: var(--card-white); }
  .back-brand__name { font-weight: 700; font-size: 34px; color: var(--card-white); }
  .back-url {
    margin-top: 60px; font-size: 15px; letter-spacing: 4px; color: var(--card-white);
  }
</style>
</head>
<body>
<main class="stage">
  <section class="card card--front" aria-label="Business card front">
    <span class="edge-tab edge-tab--top"></span>
    <span class="edge-tab edge-tab--bottom"></span>

    <header class="brand">
      <span class="brand__mark"></span>
      <span class="brand__name">Caldera Film Works</span>
    </header>

    <div class="details">
      <div class="person">
        <p class="person__name">Brent Caldera</p>
        <p class="person__title">Owner/Creative Director</p>
      </div>
      <span class="divider"></span>
      <ul class="contact">
        <li class="contact__item">
          <svg class="contact__icon" viewBox="0 0 16 16"><circle cx="8" cy="8" r="8" fill="var(--brand-blue)"/><path d="M5.2 4.2l1.6-.4.9 2.2-1 .8a6 6 0 0 0 2.5 2.5l.8-1 2.2.9-.4 1.6c-3.6.3-6.9-3-6.6-6.6z" fill="#fff"/></svg>
          407-552-9031
        </li>
        <li class="contact__item">
          <svg class="contact__icon" viewBox="0 0 16 16"><circle cx="8" cy="8" r="8" fill="var(--brand-blue)"/><rect x="4" y="5" width="8" height="6" fill="#fff"/><path d="M4 5l4 3.2L12 5" stroke="var(--brand-blue)" stroke-width="1" fill="none"/></svg>
          brent@calderafilm.tv
        </li>
        <li class="contact__item">
          <svg class="contact__icon" viewBox="0 0 16 16"><circle cx="8" cy="8" r="8" fill="var(--brand-blue)"/><circle cx="8" cy="8" r="4.2" fill="none" stroke="#fff" stroke-width="1"/><path d="M3.8 8h8.4M8 3.8c-2 2.4-2 6 0 8.4M8 3.8c2 2.4 2 6 0 8.4" stroke="#fff" stroke-width="0.9" fill="none"/></svg>
          www.calderafilm.tv
        </li>
      </ul>
    </div>

    <p class="services">
      <span class="services__item">Marketing Videos</span><span class="services__item">Corporate Videos</span><span class="services__item">Conference &amp; Seminar Video Production</span>
    </p>
  </section>

  <section class="card card--back" aria-label="Business card back">
    <div class="back-brand">
      <span class="back-brand__mark"></span>
      <span class="back-brand__name">Caldera Film Works</span>
    </div>
    <p class="back-url">www.calderafilm.tv</p>
  </section>
</main>
</body>
</html>
```